Dog care service needs business card design

Our company is Paws Harbour. We provide care for dogs while their owners are away, either through home visits or a holiday stay in the homes of carefully selected minders. Our existing website & Chatterbook cover should provide all the colour cues for our business cards - namely blues, blondes and grey. We have an existing logo (provided).

www.pawsharbourcare.example.au
www.chatterbook.example/pawsharbourcareau

We wish to clearly communicate our three areas of service "dog minding, home visits, dog walking".

We would like to have the files ready for upload to Printlyne (or similar) for immediate printing.

Target Market(s)

Dog owners who love their dogs like family

Industry/Entity Type

Business

Contact Information for Business Card

Paws Harbour
Ph: 0417 358 904

Font styles to use
Sans Serif

Colors
33a6d7
3176b5

Requirements
Must have
• Logo
• Telephone number
• website
• "Dog minding, home visits, dog walking"
Should not have
• any additional illustrations beyond the logo.

```html
<!DOCTYPE html>
<html lang="en">
<head>
<meta charset="utf-8">
<title>Paws Harbour – Business Card</title>
<link rel="stylesheet" href="https://fonts.googleapis.com/css2?family=Josefin+Sans:wght@400;600;700&display=swap">
<style>
  :root {
    --page-bg: #e9eaec;
    --blue-light: #33a6d7;
    --blue-main: #3176b5;
    --blue-deep: #1d5790;
    --ink: #3b3f47;
    --ink-soft: #5b6069;
    --mark-grey: #d9dadc;
    --card-white: #ffffff;
    --card-shade: #f1f1f2;
  }
  * { box-sizing: border-box; margin: 0; padding: 0; }
  html, body {
    width: 1200px; height: 871px; overflow: hidden;
    background: var(--page-bg);
    font-family: "Josefin Sans", sans-serif;
  }
  .sheet {
    width: 1200px; height: 871px;
    display: flex; align-items: center; justify-content: center; gap: 40px;
  }
  .card {
    position: relative; width: 540px; height: 330px; overflow: hidden;
    border-radius: 3px;
    box-shadow: 0 10px 28px rgba(0,0,0,.18);
  }

  /* Back side */
  .card--back {
    background: linear-gradient(160deg, var(--blue-main) 0%, var(--blue-deep) 100%);
    color: #fff;
  }
  .back__mark {
    position: absolute; left: -40px; top: 30px; width: 250px; height: 250px;
    border-radius: 50%;
    background: radial-gradient(circle at 50% 50%, rgba(255,255,255,.55), rgba(255,255,255,.08) 70%, rgba(255,255,255,0) 72%);
  }
  .services {
    position: absolute; left: 290px; top: 60px; list-style: none;
  }
  .services li {
    display: flex; align-items: center; gap: 14px;
    font-size: 21px; font-weight: 600; letter-spacing: .5px;
    line-height: 1; margin-bottom: 14px; color: #eef4fb;
  }
  .services svg { width: 16px; height: 14px; flex: none; }
  .social {
    position: absolute; right: 26px; bottom: 24px;
    display: flex; align-items: center; gap: 12px;
    font-size: 14px; letter-spacing: .4px; color: #e3edf7;
    white-space: nowrap;
  }
  .social__square { width: 22px; height: 22px; background: #fff; opacity: .9; border-radius: 2px; }

  /* Front side */
  .card--front {
    background: linear-gradient(165deg, var(--card-white) 55%, var(--card-shade) 100%);
    color: var(--ink);
  }
  .brand {
    position: absolute; left: 34px; top: 36px;
    display: flex; align-items: center; gap: 14px;
  }
  .brand__dot { width: 46px; height: 46px; border-radius: 50%; background: var(--blue-light); }
  .brand__name { font-size: 38px; font-weight: 700; color: var(--ink); letter-spacing: -.5px; }
  .contact { position: absolute; left: 34px; top: 150px; z-index: 1; }
  .contact__name { font-size: 22px; font-weight: 700; letter-spacing: 1px; color: var(--ink-soft); margin-bottom: 22px; }
  .contact__row {
    display: flex; align-items: center; gap: 12px;
    font-size: 15px; color: var(--ink-soft); margin-bottom: 14px; letter-spacing: .3px;
  }
  .contact__row svg { width: 15px; height: 15px; flex: none; }
  .front__mark {
    position: absolute; right: -30px; bottom: -40px; width: 270px; height: 240px;
    border-radius: 50%;
    background: radial-gradient(circle at 50% 50%, var(--mark-grey), rgba(217,218,220,.25) 68%, rgba(217,218,220,0) 72%);
  }
</style>
</head>
<body>
<main class="sheet">
  <section class="card card--back" aria-label="Business card back">
    <div class="back__mark" role="img" aria-label="Large faint brand symbol area"></div>
    <ul class="services">
      <li><svg viewBox="0 0 16 14"><path d="M1 7l5 5L15 2" fill="none" stroke="#33a6d7" stroke-width="2.6" stroke-linecap="round" stroke-linejoin="round"/></svg>Dog minding</li>
      <li><svg viewBox="0 0 16 14"><path d="M1 7l5 5L15 2" fill="none" stroke="#33a6d7" stroke-width="2.6" stroke-linecap="round" stroke-linejoin="round"/></svg>home visits</li>
      <li><svg viewBox="0 0 16 14"><path d="M1 7l5 5L15 2" fill="none" stroke="#33a6d7" stroke-width="2.6" stroke-linecap="round" stroke-linejoin="round"/></svg>dog walking</li>
    </ul>
    <div class="social">
      <span class="social__square" aria-hidden="true"></span>
      <span class="social__url">www.chatterbook.example/pawsharbourcareau</span>
    </div>
  </section>

  <section class="card card--front" aria-label="Business card front">
    <div class="brand">
      <span class="brand__dot" aria-hidden="true"></span>
      <span class="brand__name">Paws Harbour</span>
    </div>
    <div class="front__mark" role="img" aria-label="Large faint brand symbol area"></div>
    <div class="contact">
      <p class="contact__name">Paws Harbour</p>
      <p class="contact__row">
        <svg viewBox="0 0 16 16"><path d="M3 2h3l1.5 3.5-2 1.3a8 8 0 0 0 3.7 3.7l1.3-2L14 10v3a1.5 1.5 0 0 1-1.6 1.5A12 12 0 0 1 1.5 3.6 1.5 1.5 0 0 1 3 2z" fill="#33a6d7"/></svg>
        0417 358 904
      </p>
      <p class="contact__row">
        <svg viewBox="0 0 16 16"><circle cx="8" cy="8" r="6.5" fill="none" stroke="#33a6d7" stroke-width="1.6"/><path d="M1.5 8h13M8 1.5c-3 3.5-3 9.5 0 13M8 1.5c3 3.5 3 9.5 0 13" fill="none" stroke="#33a6d7" stroke-width="1.3"/></svg>
        www.pawsharbourcare.example.au
      </p>
    </div>
  </section>
</main>
</body>
</html>
```